Cafe - A FRAME Design

Need to create an A frame for my café.
Logo available
Word document - has basic information we think would be good.

Name: Zorvette Café

Notes from the A-frame printers.
File Requirements
• PDF without trim, crop or registration marks
• All files to be CMYK, not RGB
• All fonts converted to outlines (paths/curves)
• Embed all images and elements
• Files to be 100% scale unless otherwise specified
• 10mm Bleed
Resolution
• Bitmap images no less than 130 DPI at full size
Pantone Colours
• If required Pantone colours must be supplied

Target Market(s)

Mainly Students - University cafe

Requirements
Must have
• Cafe name: Zorvette
Nice to have
• Might be nice to have background - that orange color same as logo - just an idea

Word document - has basic idea regarding text that should be included

```html
<!DOCTYPE html>
<html lang="en">
<head>
<meta charset="utf-8">
<title>Zorvette Café – A-Frame</title>
<link rel="stylesheet" href="https://fonts.googleapis.com/css2?family=Abril+Fatface&family=Bebas+Neue&display=swap">
<style>
  :root {
    --bg: #b7c7cb;
    --orange: #f15f24;
    --slate: #474b55;
    --pattern: #a3b7bb;
  }
  * { margin: 0; padding: 0; box-sizing: border-box; }
  html, body { width: 800px; height: 1200px; overflow: hidden; }
  body { background: var(--bg); }
  .aframe { position: relative; width: 800px; height: 1200px; background: var(--bg); }

  .brand { position: absolute; left: 80px; top: 60px; width: 660px; height: 220px; }
  .brand-dot { position: absolute; left: 10px; top: 40px; width: 150px; height: 150px; border-radius: 50%; background: var(--orange); }
  .brand-name {
    position: absolute; left: 200px; top: 48px;
    font-family: "Abril Fatface", serif; color: var(--slate);
    font-size: 96px; line-height: 1;
  }
  .brand-sub {
    position: absolute; left: 206px; top: 164px;
    font-family: "Abril Fatface", serif; color: var(--slate);
    font-size: 34px; letter-spacing: 12px; line-height: 1;
  }

  .tagline {
    position: absolute; left: 28px; top: 315px; width: 743px; height: 242px;
    background: var(--orange); border-radius: 14px;
    display: flex; flex-direction: column; align-items: center; justify-content: center;
    font-family: "Abril Fatface", serif; color: var(--slate);
    text-align: center; line-height: 0.98;
  }
  .tagline-line { font-size: 60px; }
  .tagline-amp { font-size: 60px; }

  .offer {
    position: absolute; left: 34px; top: 581px; width: 737px; height: 463px;
    border: 8px solid var(--slate); border-radius: 14px; overflow: hidden;
  }
  .offer-pattern {
    position: absolute; inset: 0;
    background: radial-gradient(ellipse at center, var(--bg) 30%, var(--pattern) 120%);
  }
  .offer-list {
    position: relative; list-style: none; height: 100%;
    display: flex; flex-direction: column; justify-content: center; align-items: center;
    gap: 10px;
  }
  .offer-item {
    font-family: "Bebas Neue", sans-serif; color: var(--slate);
    font-size: 76px; line-height: 1; white-space: nowrap;
    transform: scaleX(0.66);
  }

  .location-band {
    position: absolute; left: 0; top: 1065px; width: 800px; height: 135px;
    background: var(--slate);
    display: flex; align-items: center; justify-content: center;
  }
  .location {
    font-family: "Abril Fatface", serif; color: var(--orange);
    font-size: 62px; line-height: 1;
  }
</style>
</head>
<body>
  <main class="aframe">
    <header class="brand">
      <span class="brand-dot"></span>
      <h1 class="brand-name">Zorvette</h1>
      <p class="brand-sub">CATERING</p>
    </header>

    <section class="tagline">
      <span class="tagline-line">Your environmentally</span>
      <span class="tagline-amp">&amp;</span>
      <span class="tagline-line">sustainability focused cafe</span>
    </section>

    <section class="offer">
      <div class="offer-pattern" role="img" aria-label="Faint pattern of coffee pots, cups, beans and pastries"></div>
      <ul class="offer-list">
        <li class="offer-item">Specialty Coffee</li>
        <li class="offer-item">Fresh Food</li>
        <li class="offer-item">Pastries &amp; Drinks</li>
        <li class="offer-item">(Vegan &amp; GF) Options Available</li>
        <li class="offer-item">Catering Available</li>
      </ul>
    </section>

    <footer class="location-band">
      <p class="location">Located @ Building 417</p>
    </footer>
  </main>
</body>
</html>
```